Layout for site fence advertising - length approx. 250 cm x 125 cm

The advertising will later be printed on a PVC film and used for events or on sports fields.

Main services :
Your regional contact at
Real estate and business financing
independent insurance advice

```html
<!DOCTYPE html>
<html lang="en">
<head>
<meta charset="utf-8">
<title>Lindberg Vermögensberatung – Fence Banner</title>
<link rel="stylesheet" href="https://fonts.googleapis.com/css2?family=Montserrat:wght@300;400;600;700;800&display=swap">
<style>
  :root {
    --brand-blue: #234ea0;
    --text-grey: #5e5e5e;
    --line-grey: #5a5a5a;
    --paper: #ffffff;
    --backdrop: #eceef1;
    --photo-warm: #7a5247;
    --photo-soft: #cfc6c1;
  }
  * { margin: 0; padding: 0; box-sizing: border-box; }
  html, body {
    width: 1117px; height: 1200px; overflow: hidden;
    background: var(--backdrop);
    font-family: "Montserrat", Arial, sans-serif;
  }
  .banner {
    position: absolute; left: 0; top: 313px;
    width: 1117px; height: 573px;
    background: var(--paper);
    overflow: hidden;
  }
  .brand-mark {
    position: absolute; left: 50px; top: 51px;
    width: 124px; height: 124px;
    border: 3px solid var(--brand-blue); border-radius: 50%;
  }
  .brand-divider {
    position: absolute; left: 186px; top: 49px;
    width: 3px; height: 127px; background: var(--line-grey);
  }
  .brand-name {
    position: absolute; left: 198px; top: 84px;
    font-size: 21px; font-weight: 600; color: var(--brand-blue);
    white-space: nowrap; letter-spacing: 0.2px;
  }
  .brand-tagline {
    position: absolute; left: 197px; top: 117px;
    font-size: 16.4px; font-weight: 600; color: var(--text-grey);
    white-space: nowrap; letter-spacing: 0.3px;
  }
  .headline { position: absolute; left: 0; top: 0; }
  .headline span { position: absolute; white-space: nowrap; line-height: 1; }
  .headline .your { left: 87px; top: 212px; font-size: 31px; font-weight: 800; color: var(--brand-blue); }
  .headline .regional { left: 64px; top: 231px; font-size: 70px; font-weight: 300; color: var(--text-grey); letter-spacing: 0.5px; }
  .headline .contact { left: 172px; top: 296px; font-size: 34px; font-weight: 800; color: var(--brand-blue); }
  .services { position: absolute; left: 62px; top: 352px; list-style: none; }
  .services li {
    display: flex; align-items: center; height: 32px; margin-bottom: 14px;
    font-size: 25px; font-weight: 700; color: var(--text-grey); white-space: nowrap;
  }
  .services svg { width: 32px; height: 32px; margin-right: 15px; flex: none; }
  .bottom-rule {
    position: absolute; left: 185px; top: 464px;
    width: 3px; height: 109px; background: var(--line-grey);
  }
  .portrait-ring { position: absolute; left: 0; top: 0; width: 1117px; height: 573px; }
  .portrait {
    position: absolute; left: 643px; top: 64px;
    width: 420px; height: 420px; border-radius: 50%;
    background: linear-gradient(180deg, var(--photo-warm) 0%, var(--photo-soft) 100%);
  }
</style>
</head>
<body>
  <main class="banner">
    <div class="brand-mark"></div>
    <div class="brand-divider"></div>
    <div class="brand-name">Lindberg Vermögensberatung GmbH</div>
    <div class="brand-tagline">Finanzieren, Versichern, Vorsorgen</div>

    <h1 class="headline">
      <span class="your">Your</span>
      <span class="regional">regional</span>
      <span class="contact">contact at</span>
    </h1>

    <ul class="services">
      <li>
        <svg viewBox="0 0 32 32" fill="none" stroke="var(--brand-blue)" stroke-width="1.6" stroke-linejoin="round" stroke-linecap="round">
          <path d="M5 14 L16 4 L27 14"/>
          <path d="M8 12 V20 M24 12 V20"/>
          <rect x="13" y="11" width="6" height="5"/>
          <path d="M3 24 L9 20 L15 23 L19 22 L23 24 L29 21"/>
          <path d="M3 28 L10 27 L16 28 L22 27 L29 28"/>
        </svg>
        Real estate and business financing
      </li>
      <li>
        <svg viewBox="0 0 32 32" fill="none" stroke="var(--brand-blue)" stroke-width="1.6" stroke-linejoin="round" stroke-linecap="round">
          <path d="M16 3 L23 6 V12 C23 17 20 20 16 22 C12 20 9 17 9 12 V6 Z"/>
          <path d="M13 12 L15.5 14.5 L19.5 10"/>
          <path d="M3 17 L7 23 L11 26 V30 M29 17 L25 23 L21 26 V30"/>
        </svg>
        Independent insurance advice
      </li>
    </ul>

    <div class="bottom-rule"></div>

    <svg class="portrait-ring" viewBox="0 0 1117 573" aria-hidden="true">
      <defs>
        <mask id="ring-gap">
          <rect width="1117" height="573" fill="#fff"/>
          <polygon points="853,274 1117,300 1117,380" fill="#000"/>
        </mask>
      </defs>
      <path fill="var(--brand-blue)" fill-rule="evenodd" mask="url(#ring-gap)"
        d="M605,290 a243,243 0 1,0 486,0 a243,243 0 1,0 -486,0 Z
           M612,279 a235,235 0 1,0 470,0 a235,235 0 1,0 -470,0 Z"/>
    </svg>
    <div class="portrait" role="img" aria-label="Portrait photo of the regional financial advisor"></div>
  </main>
</body>
</html>
```